Board menu for "Olla Dorada" food truck

Summary
**********************************
We need a menu design for a food truck. The menu will be printed and placed in the food truck side, so that customers can read it while standing one or two meters away from it. The size of the printed menu should be (width x height): 108cm x 70cm. The food truck is located in Panama and the menu language is Spanish.

Menu Sections
**************************************
The menu is divided in the following 5 sections:

1. Main Courses: This section should take most of the menu space. There are 5 menu items in this section. Each item has a Name, Description, Picture, Price (of item alone), and Price (of item in combo). Please note that for all items, combo means adding one beverage and one side. The added price is $1.50 to make any main course a combo. So it might we better to say “make it a combo for +$1.50” versus say “alone $5.50, in combo $7.00”.

2. Side Orders: This section has 2 menu items. Each item has a Name and Price. There are no pictures for this section or items.

3. Soups: This section has a Picture and Description for the entire section plus 2 menu items. Each menu item has a Name and Price.

4. Bakery: This section has a Picture for the entire section plus 5 menu items. Each item has a Name and a Price.

5. Beverages: This section has 5 menu items. Each menu item has a Name and a Price. There are no pictures for this section or items.

Attachments
*******************************************
We are attaching a zip file with picture of the exterior of the food truck. The menu will go in the space between the food truck’s window and the light switch, leaving ample space between those boundaries and the menu. The trash can shown in the picture has been relocated so it will not obstruct the menu view.

The zip file also contains the pictures for the 5 menu items in the Main Courses section, the picture for the Soups section, and the picture for the Bakery section (the bakery picture is provided as a place holder. We will provide a better bakery picture to the winning design to replace this one). For information purposes, the zip file also contains the food truck logo. The logo will not go in the menu. The brand and social media icons will go elsewhere in the truck.

The zip file also contains the file “menu information.xlsx”. This file has the following sheets:

Sections: Contains a column with the section name in English and another one with the section name in Spanish (which should be used in the menu). For the Soups section, contains a column with the section’s Description and Picture Name. For the Bakery section, contains a column with the section’s Picture Name.

Main Courses: Contains a column for each of the following: Item Name, Item Description, Item Picture Name, Item Price, Item Price (in combo). Again, we leave it to the designer’s discretion to use +$1.50 (or similar) for the combo versus publishing the full combo price.

Side Orders: Contains columns for Item Name and Item Price.

Soups: Contains columns for Item Name and Item Price.

Bakery: Contains columns for Item Name and Item Price. In the case of the Donuts item, there is an addition column with the Available Flavors.

Beverages: Contains columns for Item Name and Item Price. In the case of the Sodas item, there is an additional column with the Available Flavors.

A note about file encoding: the excel file contains texts with Spanish language special characters. It is encoded in the Windows-1252 encoding which I think is the Excel default for Western European languages. For those having trouble with this encoding, I included a “menu information csv” folder in the zip file with all the sheets in csv format encoded using UTF-8.
Updates

Target Market(s)

The truck sells fast food to drivers commuting from Panama City to towns in the west of the city. The average customer is a middle-class professional with a car. The truck is located in one of our gas stations so most customers stop to fuel their cars and grab something to eat for the ride home.

Font styles to use
Sans Serif

Colors

Designer to choose colors to be used in the design.

Requirements
Must have
• We would like to make emphasis in the main courses. Since they required preparation, they are not displayed, unlike other items like bakery, soups and beverages that are always ready and displayed. Having their pictures and descriptions on the menu will allows the customer to quickly figure out what main courses are available.

```html
<!DOCTYPE html>
<html lang="es">
<head>
<meta charset="utf-8">
<title>Olla Dorada — Menú</title>
<link href="https://fonts.googleapis.com/css2?family=Montserrat:wght@400;500;700&family=Yellowtail&display=swap" rel="stylesheet">
<style>
  :root{
    --blue:#113c7e;
    --red:#b3161c;
    --red-text:#c8161e;
    --white:#ffffff;
    --ink:#111111;
    --price-on-blue:#e0262c;
    --price-on-red:#7e0c10;
  }
  *{box-sizing:border-box;margin:0;padding:0}
  html,body{width:1200px;height:778px;overflow:hidden;background:var(--white)}
  .menu-board{position:relative;width:1200px;height:778px;font-family:"Montserrat",sans-serif;color:var(--white)}
  .brand{position:absolute;top:0;left:0;width:1200px;height:128px;display:flex;align-items:center;justify-content:center;gap:18px}
  .brand-name{font-family:"Montserrat",sans-serif;font-weight:700;font-size:34px;letter-spacing:1px;color:var(--ink)}
  .brand-mark{width:90px;height:90px;border:4px solid var(--ink);border-radius:50%}
  .mains{position:absolute;top:128px;left:0;width:1200px;height:297px;display:grid;grid-template-columns:repeat(5,240px)}
  .main-item{display:flex;flex-direction:column;overflow:hidden}
  .main-item.blue{background:var(--blue)}
  .main-item.red{background:var(--red)}
  .item-title{height:57px;display:flex;align-items:center;justify-content:center;font-family:"Yellowtail",cursive;font-weight:400;font-size:32px;line-height:1;white-space:nowrap}
  .item-photo{height:154px}
  .item-info{padding:10px 11px 0;font-size:7.3px;line-height:11.8px;text-transform:uppercase;letter-spacing:.3px;text-align:justify}
  .item-price{display:block;text-align:left;font-weight:500}
  .blue .item-price{color:var(--price-on-blue)}
  .red .item-price{color:var(--price-on-red)}
  .item-price span{display:inline-block;width:54px}
  .sections{position:absolute;top:425px;left:0;width:1200px;height:353px;display:grid;grid-template-columns:repeat(5,240px)}
  .section{display:flex;flex-direction:column}
  .section-title{height:71px;background:var(--white);display:flex;align-items:center;justify-content:center;font-family:"Yellowtail",cursive;font-weight:400;font-size:34px;color:var(--red-text);white-space:nowrap}
  .section-photo{height:154px}
  .section-body{flex:1;padding:15px 12px 0;font-size:11.2px;line-height:13.6px;text-transform:uppercase;letter-spacing:.2px}
  .section.blue .section-body{background:var(--blue)}
  .section.red .section-body{background:var(--red)}
  .section-fill{flex:1;background:var(--red)}
  .price-row{display:flex;justify-content:space-between}
  .price-row .price{letter-spacing:1.5px}
  .flavors{font-size:7px;line-height:9px;text-align:center;letter-spacing:.3px}
</style>
</head>
<body>
<main class="menu-board">
  <header class="brand">
    <span class="brand-name">OLLA DORADA</span>
    <span class="brand-mark"></span>
  </header>

  <section class="mains">
    <article class="main-item blue">
      <h2 class="item-title">El Rinconcito</h2>
      <div class="item-photo" role="img" aria-label="Foto de emparedado de jamón y queso en pan flauta" style="background:linear-gradient(160deg,#8a4a2a,#d8a070 55%,#c7423a)"></div>
      <p class="item-info">Emparedado de queso americano y jamones variados en pan flauta, a la casa.
        <span class="item-price"><span>A la carte:</span>$2.50</span>
        <span class="item-price"><span>Combo:</span>$4.00</span></p>
    </article>
    <article class="main-item red">
      <h2 class="item-title">Chorizazo</h2>
      <div class="item-photo" role="img" aria-label="Foto de choripán con chimichurri y papas fritas" style="background:linear-gradient(160deg,#e9d6d2,#c99a5e 50%,#d4363a)"></div>
      <p class="item-info">Choripán de chorizo criollo jumbo con chimichurri de la casa en pan baguette.
        <span class="item-price"><span>A la carte:</span>$3.00</span>
        <span class="item-price"><span>Combo:</span>$4.50</span></p>
    </article>
    <article class="main-item blue">
      <h2 class="item-title">Mi Tostón</h2>
      <div class="item-photo" role="img" aria-label="Foto de patacones con pollo y salsa de ajo" style="background:linear-gradient(160deg,#1b3a80,#c9a040 50%,#e8e2cc)"></div>
      <p class="item-info">Pollo, cebolla caramelizada y salsa de ajo con cilantro sobre cama de patacones.
        <span class="item-price"><span>A la carte:</span>$3.25</span>
        <span class="item-price"><span>Combo:</span>$4.75</span></p>
    </article>
    <article class="main-item red">
      <h2 class="item-title">El Consentido</h2>
      <div class="item-photo" role="img" aria-label="Foto de emparedado de pollo a la plancha en pan baguette" style="background:linear-gradient(160deg,#6e4a35,#e6d8c4 50%,#c97a5a)"></div>
      <p class="item-info">Emparedado de pollo a la plancha, queso mozzarella, cebolla caramelizada, tomate y salsa ranch en pan baguette.
        <span class="item-price"><span>A la carte:</span>$4.50</span>
        <span class="item-price"><span>Combo:</span>$6.00</span></p>
    </article>
    <article class="main-item blue">
      <h2 class="item-title">La Parrandera</h2>
      <div class="item-photo" role="img" aria-label="Foto de hamburguesa con papas fritas" style="background:linear-gradient(160deg,#7a4a2e,#e2b060 50%,#c7333a)"></div>
      <p class="item-info">1/2 libra de hamburguesa angus, queso americano, cebolla caramelizada, tomate, bacon y salsa de la casa en pan de miel con semillas de amapola.
        <span class="item-price"><span>A la carte:</span>$5.50</span>
        <span class="item-price"><span>Combo:</span>$7.00</span></p>
    </article>
  </section>

  <section class="sections">
    <div class="section red">
      <h2 class="section-title">Side Orders</h2>
      <div class="section-photo" role="img" aria-label="Foto de papas fritas" style="background:linear-gradient(170deg,#c8955c,#e8b040 55%,#f2e6d0)"></div>
      <div class="section-body">
        <p class="price-row"><span>Papas fritas</span><span class="price">$1.00</span></p>
        <p class="price-row"><span>Patacones</span><span class="price">$1.00</span></p>
      </div>
    </div>
    <div class="section blue">
      <h2 class="section-title">Soups</h2>
      <div class="section-photo" role="img" aria-label="Foto de sopa de pollo en vaso" style="background:linear-gradient(160deg,#d0403e,#e8e4d8 45%,#1e1e22)"></div>
      <div class="section-body">
        <p class="price-row"><span>Sopa de pollo<br>con arroz</span><span class="price">$2.95</span></p>
        <p class="price-row"><span>Sopa de lenteja y<br>carne con arroz</span><span class="price">$2.95</span></p>
      </div>
    </div>
    <div class="section red">
      <h2 class="section-title">Bakery</h2>
      <div class="section-photo" role="img" aria-label="Foto de pasteles horneados" style="background:linear-gradient(160deg,#2a2a2a,#d09a5a 50%,#3a3a3a)"></div>
      <div class="section-body">
        <p class="price-row"><span>Enchilada de carne</span><span class="price">$1.50</span></p>
        <p class="price-row"><span>Pastelito de pollo</span><span class="price">$1.25</span></p>
        <p class="price-row"><span>Pañuelo de queso</span><span class="price">$1.00</span></p>
        <p class="price-row"><span>Cañón de guayaba</span><span class="price">$0.85</span></p>
        <p class="price-row"><span>Donas rellenas</span><span class="price">$0.85</span></p>
        <p class="flavors">Crema pastelera, fresa, manzana, maracuyá</p>
      </div>
    </div>
    <div class="section blue">
      <h2 class="section-title">Beverages</h2>
      <div class="section-photo" role="img" aria-label="Foto de chicheme y maíz" style="background:linear-gradient(160deg,#5a3a28,#f0e8d0 40%,#e8b840 70%,#e06a30)"></div>
      <div class="section-body">
        <p class="price-row"><span>Chicheme chorrerano</span><span class="price">$1.60</span></p>
        <p>(16oz)</p>
        <p class="price-row"><span>Chica del día (16oz)</span><span class="price">$1.00</span></p>
        <p class="price-row"><span>Sodas (12oz)</span><span class="price">$1.00</span></p>
        <p class="price-row"><span>Agua (16oz)</span><span class="price">$0.75</span></p>
        <p class="price-row"><span>Café de altura (8oz)</span><span class="price">$1.00</span></p>
      </div>
    </div>
    <div class="section red">
      <h2 class="section-title">Others</h2>
      <div class="section-fill"></div>
    </div>
  </section>
</main>
</body>
</html>
```